Lanternleaf - Fresh Asian Cuisine Menu

We need to redo our menu to include pictures of food items. Our restaurant is vibrant, trendy, upscale Chinese cuisine

Requirements
Must have
• Must fit on 8.5x11 paper. We can remove the About Us section if needed but menu cannot be more than 6 pages total. Must include pictures of menu items

```html
<!DOCTYPE html>
<html lang="en">
<head>
<meta charset="utf-8">
<title>Lanternleaf - Fresh Asian Cuisine Menu</title>
<link href="https://fonts.googleapis.com/css2?family=Audiowide&family=Cinzel:wght@700&family=Roboto:wght@400;500&family=Roboto+Condensed:wght@500&display=swap" rel="stylesheet">
<style>
:root{
  --ink:#0e0e0e;
  --red:#e0161f;
  --paper:#ffffff;
  --stage:#e7e7e8;
  --muted:#cfcfcf;
  --grey-text:#444;
}
*{margin:0;padding:0;box-sizing:border-box}
html,body{width:989px;height:1200px;overflow:hidden;background:var(--stage)}
body{position:relative;font-family:"Roboto",sans-serif}
.page{position:absolute;overflow:hidden}
.abs{position:absolute}
.frame{position:absolute;border:1.5px solid var(--red)}
.display{font-family:"Audiowide",sans-serif;text-transform:uppercase;letter-spacing:.5px}
.photo{position:absolute}

/* front */
.front{left:142px;top:96px;width:334px;height:464px;background:var(--ink);color:var(--paper)}
.brand{position:absolute;left:0;right:0;top:46px;text-align:center}
.brand-name{font-family:"Cinzel",serif;font-weight:700;font-size:25px;letter-spacing:1px;display:inline-flex;align-items:center;gap:6px}
.brand-name i{display:inline-block;width:14px;height:14px;border-radius:50%;background:var(--red)}
.brand-sub{font-family:"Cinzel",serif;font-weight:700;font-size:7px;letter-spacing:2px;margin-top:2px;padding-left:60px}
.tagline{position:absolute;left:0;right:0;top:98px;text-align:center;font-size:8.5px}
.tagline:after{content:"";display:block;width:190px;height:1px;background:var(--red);margin:3px auto 0}
.nav{position:absolute;left:0;right:0;text-align:center;font-size:6px}
.nav span{padding:0 4px;border-right:1px solid var(--red)}
.nav span:last-child{border-right:0}
.strip{position:absolute;left:40px;top:310px;width:254px;height:62px;background:var(--paper);display:flex;gap:3px;padding:3px}
.strip div{flex:1}
.hours-title{position:absolute;left:0;right:0;top:384px;text-align:center;font-size:7px}
.hours{position:absolute;left:0;right:0;top:396px;text-align:center;font-size:4.6px}
.addr{position:absolute;left:0;right:0;top:420px;text-align:center;font-size:7px}
.call{position:absolute;left:0;right:0;top:432px;text-align:center;font-size:4.2px}
.rule{position:absolute;height:1px;background:var(--red)}

/* back */
.back{left:512px;top:96px;width:330px;height:464px;background:var(--paper)}
.back-dark{position:absolute;left:0;top:0;width:166px;height:464px;background:var(--ink)}
.heading-line{position:absolute;font-size:7px;text-align:center;display:flex;align-items:center;gap:5px}
.heading-line:before,.heading-line:after{content:"";flex:1;height:1px;background:var(--red)}
.about-text{position:absolute;left:30px;top:64px;width:112px;color:#ddd;font-size:4.6px;line-height:1.55;text-align:center}
.about-text p{margin-bottom:7px}
.contact{position:absolute;left:184px;width:114px;text-align:center;font-size:5px;color:#222;line-height:1.5}
.back-name{position:absolute;left:0;width:166px;top:366px;display:flex;align-items:center;justify-content:center;gap:5px;font-family:"Roboto",sans-serif;font-weight:500;font-size:8px;letter-spacing:1px;color:var(--red)}
.back-name i{display:inline-block;width:7px;height:7px;border-radius:50%;background:var(--red)}

/* inner */
.inner-left{left:140px;top:600px;width:348px;height:518px;background:var(--paper)}
.inner-right{left:488px;top:600px;width:354px;height:518px;background:var(--paper)}
.inner-dark{position:absolute;left:0;top:0;width:178px;height:518px;background:var(--ink)}
.section-tag{position:absolute;background:var(--ink);color:var(--paper);border:1.5px solid var(--ink);outline:1px solid var(--paper);outline-offset:-3.5px;font-size:10.5px;padding:3px 12px;border-radius:3px}
.on-dark .section-tag{background:var(--paper);color:var(--ink)}
.sub{position:absolute;font-size:6px;font-family:"Roboto",sans-serif;font-weight:500;text-decoration:underline;text-underline-offset:2px}
.icon{position:absolute}
.item{position:absolute}
.item h4{display:flex;justify-content:space-between;font-family:"Roboto Condensed",sans-serif;font-weight:500;font-size:7px;color:var(--red);letter-spacing:.2px}
.item p{font-size:4.6px;line-height:1.45;color:var(--grey-text);margin-top:2px;width:92%}
.on-dark .item p{color:#ccc}
.pic-band{position:absolute;left:30px;top:222px;width:285px;height:80px;background:var(--ink);display:flex;gap:3px;padding:4px}
.pic-band div{flex:1}
</style>
</head>
<body>

<!-- FRONT PAGE -->
<section class="page front">
  <div class="frame" style="left:15px;top:16px;width:305px;height:434px"></div>
  <div class="brand">
    <div class="brand-name"><i></i>LANTERNLEAF</div>
    <div class="brand-sub">FRESH ASIAN CUISINE</div>
  </div>
  <div class="tagline display">Serving the best asian cuisine</div>

  <svg class="abs" style="left:78px;top:118px" width="178" height="144" viewBox="0 0 178 144">
    <polygon points="30,72 89,2 148,72 89,142" fill="none" stroke="#e0161f" stroke-width="1.5"/>
    <polygon points="4,72 30,50 30,94" fill="none" stroke="#e0161f" stroke-width="1.2"/>
    <polygon points="174,72 148,50 148,94" fill="none" stroke="#e0161f" stroke-width="1.2"/>
  </svg>
  <div class="photo" role="img" aria-label="Steamed bao buns, glazed chicken and chopsticks on a plate"
       style="left:98px;top:124px;width:138px;height:132px;border-radius:40px;border:2px solid var(--red);background:linear-gradient(140deg,#e9e4da 0%,#9c8f7c 45%,#b4552a 75%,#3a2a20 100%)"></div>
  <div class="abs" style="left:60px;top:150px;width:1px;height:80px;background:var(--red)"></div>
  <div class="abs" style="left:273px;top:150px;width:1px;height:80px;background:var(--red)"></div>

  <div class="nav display" style="top:272px"><span>Appetizers</span><span>Entrees</span><span>Noodles and Rice</span><span>Vegetarian Dishes</span></div>
  <div class="nav display" style="top:290px"><span>Kids Menu</span><span>Desserts</span><span>Lantern Bar Menu</span><span>Lunch Menu</span></div>

  <div class="strip">
    <div role="img" aria-label="Plated vegetable salad" style="background:linear-gradient(135deg,#5e7a3a,#c9b89a,#8a3b2a)"></div>
    <div role="img" aria-label="Pan fried dumplings with scallions" style="background:linear-gradient(135deg,#3b5a2a,#d8b26c,#a77b3d)"></div>
    <div role="img" aria-label="Braised eggplant dish" style="background:linear-gradient(135deg,#c7c2bb,#5b3a5a,#7a6a3a)"></div>
  </div>

  <div class="rule" style="left:126px;top:388px;width:82px"></div>
  <div class="hours-title display" style="top:383px"><span style="background:var(--ink);padding:0 4px">Open Hours</span></div>
  <div class="hours">Mon - Thu 11:00 am - 3:00 pm &amp; 5:00 pm - 9:00 pm &nbsp;/&nbsp; Fri - Sat 11:00 am - 10:00 pm &nbsp;/&nbsp; Sun 11:00 am - 9:00 PM</div>
  <div class="rule" style="left:150px;top:414px;width:34px"></div>
  <div class="addr display">Address information here</div>
  <div class="call">Call Us : 555-014-2270 &nbsp;&nbsp;|&nbsp;&nbsp; www.lanternleafkitchen.com</div>
</section>

<!-- BACK PAGE -->
<section class="page back">
  <div class="back-dark"></div>
  <div class="frame" style="left:18px;top:18px;width:296px;height:430px"></div>

  <div class="heading-line display" style="left:36px;top:48px;width:108px;color:var(--paper)">About us</div>
  <div class="about-text">
    <p>At Lanternleaf, we pride ourselves in serving fresh, authentic Sichuan Chinese cuisine delicately prepared by our expertly trained Chefs.</p>
    <p>Sichuan cuisine comes from southwest China between the Sichuan Basin and the Tibetan Plateau. It is known for being both very spicy and flavorful, much like our own southern Louisiana cuisine.</p>
    <p>Our Executive Chef, Wei Lan grew up in the southwestern Chinese province of Sichuan, where she began her training at fifteen years old under her grandfather's mentorship. Chef Lan became an acclaimed chef in the province, opening several restaurants and traveling throughout China to cook for many guests. She has worked in restaurants across the United States and we now welcome her to her new home in Riverton, Louisiana.</p>
    <p>We are very excited to bring to Riverton the authenticity of Chinese cuisine and hope you enjoy your experience dining with us.</p>
  </div>
  <div class="back-name"><i></i>LANTERNLEAF</div>

  <div class="heading-line display" style="left:184px;top:48px;width:114px;color:var(--ink)">Contact us</div>
  <div class="contact" style="top:82px">88 Harbor Lantern Ave, Suite 12<br>Riverton LA 70990</div>
  <div class="contact" style="top:106px">555-014-2270</div>
  <div class="contact" style="top:123px">www.lanternleafkitchen.com</div>
  <div class="contact" style="top:141px">www.social.example/LanternleafKitchen</div>
  <div class="photo" role="img" aria-label="Street map showing the restaurant location"
       style="left:184px;top:170px;width:113px;height:142px;border:1.5px solid var(--red);background:linear-gradient(160deg,#eef0f2,#dde3ea)"></div>
  <div class="photo" role="img" aria-label="Chopsticks lifting a bundle of noodles"
       style="left:192px;top:336px;width:138px;height:128px;background:radial-gradient(ellipse at 50% 90%,#f1e4b4 0%,#f6efd6 40%,rgba(255,255,255,0) 70%)"></div>
</section>

<!-- INNER LEFT: APPETIZERS -->
<section class="page inner-left">
  <div class="frame" style="left:16px;top:18px;width:314px;height:482px"></div>
  <svg class="icon" style="left:166px;top:28px" width="16" height="18" viewBox="0 0 16 18" aria-hidden="true">
    <line x1="8" y1="0" x2="8" y2="18" stroke="#e0161f" stroke-width="1.4"/>
    <circle cx="8" cy="6" r="3" fill="#e0161f"/><circle cx="8" cy="12" r="3" fill="#e0161f"/>
  </svg>
  <div class="section-tag display" style="left:118px;top:49px">Appetizers</div>

  <div class="item" style="left:38px;top:84px;width:118px"><h4>EDAMAME<span>$ 4</span></h4><p>Seasoned &amp; boiled soy bean</p></div>
  <div class="item" style="left:38px;top:113px;width:118px"><h4>SCALLION PANCAKES<span>$ 6</span></h4><p>Traditional Chinese flatbread folded with oil and minced scallions and pan fried</p></div>
  <div class="item" style="left:38px;top:149px;width:118px"><h4>LANTERNLEAF LETTUCE WRAPS<span>$ 4</span></h4><p>Seasoned ground chicken drizzled with our top secret homemade sauce served with lettuce wraps</p></div>
  <div class="item" style="left:38px;top:192px;width:118px"><h4>SALT &amp; PEPPER CALAMARI<span>$ 6</span></h4><p>Traditional Chinese flatbread folded with oil and minced scallions and pan fried</p></div>

  <div class="item" style="left:190px;top:82px;width:120px"><h4>CRISPY MALA BEEF JERKY<span>$ 9</span></h4><p>Dry fried shredded beef with various peppers in sesame and peppercorn oil</p></div>
  <div class="item" style="left:190px;top:118px;width:120px"><h4>FRIED CHICKEN DUMPLINGS (6)<span>$ 6</span></h4><p>Chinese dumpling stuffed with Chicken, Shiitake mushrooms and bamboo shoots</p></div>
  <div class="item" style="left:190px;top:154px;width:120px"><h4>RED OIL DUMPLINGS (6)<span>$ 7</span></h4><p>Chicken filled dumplings in Sichuan red oil sauce drizzled with sesame</p></div>
  <div class="item" style="left:190px;top:190px;width:120px"><h4>PORK EGG ROLLS (2)<span>$ 4</span></h4><p>Hand rolled with julienned veggies with our sweet n' sour mustard sauce</p></div>

  <div class="pic-band">
    <div role="img" aria-label="Stir fried chicken with peppers" style="background:linear-gradient(135deg,#2a1a12,#8a3a1a,#c9c4b8)"></div>
    <div role="img" aria-label="Chicken dumplings on a plate" style="background:linear-gradient(135deg,#3a3a3a,#d8c38a,#9a7a3a)"></div>
    <div role="img" aria-label="Crispy shrimp in a red bowl" style="background:linear-gradient(135deg,#b01414,#e08a3a,#f0d9a0)"></div>
  </div>

  <div class="item" style="left:38px;top:319px;width:118px"><h4>BUDDHA BANG SHRIMP<span>$ 9</span></h4><p>Crispy fried shrimp tossed in our creamy spicy sauce</p></div>
  <div class="item" style="left:38px;top:355px;width:118px"><h4>DRUNKEN CHICKEN<span>$ 8</span></h4><p>Chicken, Thai chili in a house made spicy sauce</p></div>
  <div class="item" style="left:38px;top:390px;width:118px"><h4>SICHUAN SPICED BEEF<span>$ 9</span></h4><p>Beef Shank, beef tripe, cilantro, peanuts and celery</p></div>
  <div class="item" style="left:38px;top:427px;width:118px"><h4>BEEF CRISPY BOTTOM BAO<span>$ 10</span></h4><p>Pan fried crispy bottom Bao, stuffed with beef, drizzled with scallion and sesame (Fresh made to order, takes at least 20 mins to serve)</p><p style="margin-top:5px">Add Shrimp $1</p></div>

  <div class="item" style="left:190px;top:321px;width:120px"><h4>VEGETARIAN SPRING ROLLS (3)<span>$ 4</span></h4><p>Traditional Asian Roll served with a sweet chili sauce</p></div>
  <div class="item" style="left:190px;top:357px;width:120px"><h4>GARLIC CUCUMBER SALAD<span>$ 7</span></h4><p>Sliced cucumber with a garlic vinaigrette</p></div>
  <div class="item" style="left:190px;top:392px;width:120px"><h4>HOT N' SOUR SOUP<span>$ 4</span></h4><p>Tangy broth with Bamboo shoot, wood ear mushrooms, tofu, egg and carrots</p></div>
  <div class="item" style="left:190px;top:430px;width:120px"><h4>WEST LAKE SOUP<span>$ 4</span></h4><p>Light creamy soup with ground beef, diced Shiitake mushroom, tofu, bamboo shoots, egg white and cilantro</p></div>
</section>

<!-- INNER RIGHT: ENTREES -->
<section class="page inner-right">
  <div class="inner-dark"></div>
  <div class="frame" style="left:18px;top:16px;width:320px;height:484px"></div>

  <div class="on-dark">
    <svg class="icon" style="left:80px;top:36px" width="18" height="16" viewBox="0 0 18 16" aria-hidden="true">
      <path d="M1 8 H17 A8 7 0 0 1 1 8 Z" fill="#fff"/><rect x="6" y="3" width="6" height="4" rx="1" fill="#fff"/>
    </svg>
    <div class="section-tag display" style="left:45px;top:59px">Entrees</div>
    <div class="sub" style="left:0;width:178px;text-align:center;top:84px;color:var(--paper)">CHEF SPECIALTIES</div>

    <div class="item" style="left:34px;top:114px;width:128px"><h4>JASMINE TEA SMOKED DUCK<span>$ 24</span></h4><p>Boneless half duck served with thinly sliced cucumber, scallion, house made duck sauce and soft flour wrap</p></div>
    <div class="item" style="left:34px;top:158px;width:128px"><h4>SIZZLING CUMIN LAMB<span>$ 16</span></h4><p>Tender pieces of lamb rubbed in cumin, Sichuan peppers, red and green bell peppers and onions</p></div>
    <div class="item" style="left:34px;top:203px;width:128px"><h4>CHEF LAN'S SPICY BEEF<span>$ 16</span></h4><p>Angus beef in house made green peppercorn sauce with Chinese cabbage, sprouts &amp; celery garnished with fresh Sichuan peppercorn, Thai chili and cilantro</p></div>
    <div class="item" style="left:34px;top:256px;width:128px"><h4>CHEF LAN'S SPICY FISH<span>$ 17</span></h4><p>Fish filet in house made green peppercorn sauce with Chinese cabbage, sprouts &amp; celery garnished with fresh Sichuan peppercorn, Thai chili and cilantro</p></div>
    <div class="item" style="left:34px;top:309px;width:128px"><h4>GENERAL TSO'S SCALLOPS<span>$ 18</span></h4><p>The perfect combination of tender scallops marinated in a sweet chili sauce with broccoli and red peppers</p></div>

    <div class="photo" role="img" aria-label="Spicy Sichuan fish in a red bowl with herbs"
         style="left:40px;top:358px;width:114px;height:114px;border-radius:34px;border:2px solid var(--red);background:radial-gradient(circle,#4e6a2a 0%,#b8421a 45%,#6a1a10 100%)"></div>
  </div>

  <svg class="icon" style="left:256px;top:36px" width="18" height="16" viewBox="0 0 18 16" aria-hidden="true">
    <path d="M1 8 H17 A8 7 0 0 1 1 8 Z" fill="#e0161f"/><rect x="6" y="3" width="6" height="4" rx="1" fill="#e0161f"/>
  </svg>
  <div class="section-tag display" style="left:219px;top:61px">Entrees</div>
  <div class="sub" style="left:178px;width:176px;text-align:center;top:86px;color:var(--ink);text-decoration:none">BEEF &amp; PORK</div>

  <div class="item" style="left:194px;top:114px;width:128px"><h4>DANCING BEEF<span>$ 24</span></h4><p>Angus Beef slices on a bed of sizzling rice crackers, black peppercorn and Thai chili</p></div>
  <div class="item" style="left:194px;top:151px;width:128px"><h4>OYSTER BEEF<span>$ 16</span></h4><p>Tender cuts of steak wok fried with onions and marinated in a homemade oyster sauce</p></div>
  <div class="item" style="left:194px;top:188px;width:128px"><h4>DOUBLE PEPPER BEEF<span>$ 16</span></h4><p>Angus steak with peppercorn, Thai chili, Serrano pepper and tofu and rice noodles</p></div>
  <div class="item" style="left:194px;top:225px;width:128px"><h4>BLACK PEPPER STEAK<span>$ 17</span></h4><p>Tender cuts of steak mixed with onions and red and green bell peppers</p></div>
  <div class="item" style="left:194px;top:262px;width:128px"><h4>SINGAPORE BABY BACK RIBS<span>$ 18</span></h4><p>Tender Baby back ribs rubbed in a Thai inspired sweet tangy glaze</p></div>
  <div class="item" style="left:194px;top:299px;width:128px"><h4>DANCING PORK BELLY<span>$ 17</span></h4><p>Braised Pork Belly on sizzling rice cracker</p></div>
  <div class="item" style="left:194px;top:329px;width:128px"><h4>TWICE COOKED PORK<span>$ 18</span></h4><p>Stir fried Pork Belly slices with leek and fermented black beans</p></div>

  <div class="photo" role="img" aria-label="Pork belly on crispy rice with red chili"
       style="left:198px;top:358px;width:116px;height:114px;border-radius:34px;border:2px solid var(--red);background:radial-gradient(circle,#c89a5a 0%,#7a2a14 50%,#2a1a14 100%)"></div>
</section>

</body>
</html>
```